Counseling Practice Business Card

I need a professional looking business card incorporating my new logo that was just completed. Card needs to incorporate my name and title, description of my specialty, my address, my phone number, my fax number, my email and my website URL. I need to be able to choose design on/with different paper colors and textures.
I do not have a lot of business card ideas so I am open to anything but I want bold,sharp, clear card without additional designs other than my logo (see attached file info). I am open to different color backgrounds or paper colors including black. I do not like traditional brackets around area codes in phone number or dashes between numbers in phone number. Am open to other ways of presenting including periods between numbers as appropriate. I do not know enough to know what I like yet but I want card to coordinate and work together with my logo. My practice emphasizes natural mental health interventions so any use of color (with background paper color or the blue and green in my logo) that elicits nature is nice. In addition to black, any natural brown or wood looking background might be desirable also. Most of the offerings so far look very similar and boring.

Target Market(s)

Potential therapy clients and other professionals

Contact Information for Business Card

Card information:
Marcus T. Whitfield, Ph.D.
Licensed Clinical Psychologist
Integrative Health Coach
4812 Ferndale Pkwy NW
Suite 730
Maplecrest, GA 30581
(770) 555-0142 phone
(770) 555-0186 fax
drmarcuswhitfield@kelvora.com
pathbloomcounseling.com

Font styles to use
Serif
Sans Serif
Other font styles liked:
• anything that you think looks crisp, clear and easily readable

Requirements
Must have
• Any color used should coordinate with my logo design (see attached files).
• Card should be printed horizontally so top and bottom are longest sides of rectangle.
• Background color or paper color should complement and highlight logo. Do not like a white background. black, grey, brown or any color my logo would blend well with.
Nice to have
• I would like designer to utilize color to highlight letters/name or phone-fax-web symbols.
• Bottom edge of card could be highlighted if appropriate to an idea.
Should not have
• I would NOT want the card to have a pure white background at all.
• No clear cards.
• Cards should be oriented with long sides on bottom and top, NOT sides. DO NOT LIKE THIS THIN TALL ORIENTATION.

```html
<!DOCTYPE html>
<html lang="en">
<head>
<meta charset="utf-8">
<title>Pathbloom Counseling – Business Card</title>
<link rel="stylesheet" href="https://fonts.googleapis.com/css2?family=EB+Garamond:wght@400;500&display=swap">
<style>
  :root {
    --backdrop: #a9bccb;
    --card-white: #ffffff;
    --panel-grey: #e3e3e3;
    --circle-white: #fafafa;
    --brand-blue: #2474b3;
    --text-grey: #6b6b6b;
    --band-text: #ffffff;
  }
  * { margin: 0; padding: 0; box-sizing: border-box; }
  html, body {
    width: 1200px; height: 1000px; overflow: hidden;
    background: var(--backdrop);
    font-family: "EB Garamond", Georgia, serif;
  }
  .card {
    position: absolute; left: 151px; top: 198px;
    width: 898px; height: 603px;
    background: var(--card-white);
    overflow: hidden;
  }
  .card-shapes { position: absolute; inset: 0; }
  .brand-name {
    position: absolute; left: 107px; top: 205px; width: 290px;
    text-align: center;
    color: var(--brand-blue);
    font-size: 30px; font-weight: 500; line-height: 1.15;
    letter-spacing: 1px;
  }
  .holder { position: absolute; left: 79px; top: 400px; white-space: nowrap; }
  .holder-name {
    color: var(--brand-blue); font-size: 33px; font-weight: 500;
    line-height: 1; letter-spacing: 0.4px;
  }
  .holder-title {
    color: var(--text-grey); font-size: 24px; line-height: 1;
    margin-top: 17px; letter-spacing: 3px;
  }
  .holder-title.coach { letter-spacing: 5.8px; margin-top: 14px; }
  .band-text {
    position: absolute; color: var(--band-text); font-size: 26px; line-height: 31px;
    white-space: nowrap;
  }
  .address { left: 524px; top: 96px; }
  .online { left: 558px; top: 266px; font-size: 22px; line-height: 41px; }
  .online .web { font-size: 23px; }
  .phone { left: 597px; top: 425px; font-size: 23px; line-height: 38px; }
</style>
</head>
<body>
  <div class="card">
    <svg class="card-shapes" width="898" height="603" viewBox="0 0 898 603">
      <polygon points="0,0 376,0 525,603 0,603" fill="var(--panel-grey)"
               role="img" aria-label="Soft grey panel with faint topographic contour lines"/>
      <circle cx="252" cy="232" r="145" fill="var(--circle-white)"/>

      <polygon class="band" points="435,88 898,88 898,202 460,202" fill="var(--brand-blue)"/>
      <polygon class="band" points="470,248 898,248 898,362 495,362" fill="var(--brand-blue)"/>
      <polygon class="band" points="505,405 898,405 898,519 530,519" fill="var(--brand-blue)"/>

      <circle cx="480" cy="145" r="25" fill="#fff"/>
      <path d="M480 127a11 11 0 0 0-11 11c0 8 11 22 11 22s11-14 11-22a11 11 0 0 0-11-11z" fill="var(--brand-blue)"/>
      <circle cx="480" cy="138" r="4" fill="#fff"/>

      <circle cx="515" cy="305" r="25" fill="#fff"/>
      <g fill="none" stroke="var(--brand-blue)" stroke-width="2.2">
        <circle cx="515" cy="305" r="17"/>
        <ellipse cx="515" cy="305" rx="7" ry="17"/>
        <line x1="498" y1="305" x2="532" y2="305"/>
        <path d="M501 296h28M501 314h28"/>
      </g>

      <circle cx="554" cy="466" r="25" fill="#fff"/>
      <path d="M538 463c0-7 32-7 32 0v3h-8v-3c-5-2-11-2-16 0v3h-8z" fill="var(--brand-blue)"/>
      <path d="M544 467h20l4 10h-28z" fill="var(--brand-blue)"/>
      <circle cx="554" cy="471" r="3" fill="#fff"/>
    </svg>

    <div class="brand-name">Pathbloom<br>Counseling</div>

    <div class="holder">
      <div class="holder-name">Marcus T. Whitfield, Ph.D.</div>
      <div class="holder-title">Licensed Clinical Psychologist</div>
      <div class="holder-title coach">Integrative Health Coach</div>
    </div>

    <div class="band-text address">
      4812 Ferndale Pkwy NW<br>Suite 730<br>Maplecrest, GA 30581
    </div>
    <div class="band-text online">
      <div class="email">drmarcuswhitfield@kelvora.com</div>
      <div class="web">pathbloomcounseling.com</div>
    </div>
    <div class="band-text phone">
      <div>p: 770.555.0142</div>
      <div>f: 770.555.0186</div>
    </div>
  </div>
</body>
</html>
```